Web Design Project for a Contact Center

We are a contact center catered mainly to Spain and Latin America. We currently have a web site, but the design is very poor. The site is www.vantelinkhub.com.

We would like to have something that works on a content manager, so we can maintain the page. Currently we work with Google Sites, but it could be any other.

Please see the logos attached

Target Market(s)

Companies and business that may use the services of an outsource contact center

Industry/Entity Type

Google

```html
<!DOCTYPE html>
<html lang="en">
<head>
<meta charset="utf-8">
<title>VanteLink – International Call Center</title>
<link href="https://fonts.googleapis.com/css2?family=Archivo+Narrow:wght@400;700&family=Arimo:wght@400;700&family=Playfair+Display:ital@1&family=Share+Tech+Mono&display=swap" rel="stylesheet">
<style>
:root{
  --orange:#f27a1a;
  --orange-deep:#e2620a;
  --orange-light:#f9b26b;
  --peach:#fbd6b0;
  --ink:#2b2b2b;
  --dark:#333333;
  --red:#e23a1f;
  --white:#ffffff;
  --line:#cfcfcf;
}
*{margin:0;padding:0;box-sizing:border-box}
html,body{width:1200px;height:900px;overflow:hidden;background:var(--white)}
body{position:relative;font-family:"Arimo",Arial,sans-serif;color:var(--ink)}
.abs{position:absolute}

.brand{left:236px;top:28px;display:flex;align-items:center;gap:10px}
.brand-mark{width:26px;height:26px;background:var(--orange)}
.brand-name{font-family:"Arimo",Arial,sans-serif;font-weight:700;font-size:32px;color:var(--dark);letter-spacing:1px}
.agent-photo{left:680px;top:8px;width:62px;height:84px;border-radius:30px 30px 6px 6px;background:linear-gradient(#d8d8d8,#efefef)}
.hotline{left:772px;top:70px;font-family:"Archivo Narrow",sans-serif;font-size:17px;color:var(--red)}

.nav{left:184px;top:90px;width:734px;height:36px;background:var(--orange-deep);display:flex;align-items:flex-end;padding-left:220px}
.nav a{font-family:"Archivo Narrow",sans-serif;font-weight:700;font-size:13px;color:var(--white);text-decoration:none;width:76px;height:30px;line-height:30px;text-align:center}
.nav a.is-active{background:var(--white);color:var(--orange-deep);border-radius:8px 8px 0 0;width:88px;margin-right:0}

.hero{left:184px;top:126px;width:734px;height:260px;background:linear-gradient(180deg,var(--orange-light) 0%,var(--orange) 55%,var(--orange-deep) 100%)}
.hero-title{left:214px;top:190px;font-family:"Archivo Narrow",sans-serif;font-weight:700;font-size:38px;line-height:46px;color:var(--white);text-shadow:0 1px 2px rgba(0,0,0,.25)}
.hero-title .amp{display:block;padding-left:142px}
.hero-photo{left:650px;top:136px;width:215px;height:250px;border-radius:110px 110px 0 0;background:linear-gradient(#fde3c8,#f3c79b)}
.slide-dots{left:860px;top:218px;display:flex;flex-direction:column;gap:6px}
.slide-dots span{width:22px;height:20px;border-radius:50%;border:1px solid var(--white);color:var(--white);font-size:11px;font-weight:700;text-align:center;line-height:18px;background:var(--orange-deep)}
.slide-dots span.is-current{background:var(--white);color:var(--orange-deep)}

.features{left:224px;top:382px;width:648px;height:120px;background:var(--white);border-radius:10px;box-shadow:0 2px 6px rgba(0,0,0,.25)}
.feature{top:390px;width:150px;height:108px}
.feature h3{font-family:"Archivo Narrow",sans-serif;font-weight:700;font-size:16px;margin:10px 0 8px}
.feature p{font-size:8px;line-height:11px;color:#444;height:44px}
.feature .more{display:block;width:126px;height:18px;background:var(--dark);color:var(--white);border-radius:9px;font-size:9px;line-height:18px;text-align:right;padding-right:14px;margin-top:6px}
.feature--dark{left:246px;width:146px;background:var(--dark);color:var(--white);padding:0 10px}
.feature--dark p{color:#ddd}
.feature--dark .more{background:transparent;padding-right:4px}
.feature--1{left:410px}.feature--2{left:576px}.feature--3{left:736px}
.divider-v{top:398px;width:1px;height:96px;background:var(--line)}
.arrow{top:426px}

.content{left:184px;top:508px;width:734px;height:262px;background:linear-gradient(180deg,var(--orange) 0%,var(--orange-deep) 100%)}
.welcome h2{font-family:"Archivo Narrow",sans-serif;font-weight:700;font-size:24px;color:var(--white);text-shadow:0 1px 2px rgba(0,0,0,.2)}
.welcome{left:238px;top:526px;width:300px}
.welcome p{font-size:8px;line-height:11px;color:var(--peach);margin-top:8px;font-weight:700}
.team-photo{left:244px;top:618px;width:122px;height:106px;background:linear-gradient(#e9e3dc,#b9a590)}
.care{left:380px;top:626px;width:170px}
.care h4{font-size:11px;line-height:14px;color:var(--dark);font-weight:700}
.care p{font-size:8px;line-height:11px;color:var(--peach);font-weight:700;margin-top:6px}
.col-title{font-family:"Archivo Narrow",sans-serif;font-weight:700;font-size:17px;color:var(--white)}
.voice{left:566px;top:534px}
.voice ul{list-style:none;margin-top:12px}
.voice li{font-size:8px;font-weight:700;color:var(--peach);height:18px;padding-left:12px;position:relative}
.voice li::before{content:"";position:absolute;left:0;top:2px;width:5px;height:5px;border-radius:50%;background:var(--peach)}
.news{left:726px;top:534px;width:150px}
.news .date{display:inline-block;margin-top:12px;background:var(--white);color:var(--dark);font-size:9px;font-weight:700;padding:2px 10px;border-radius:8px}
.news p{font-size:8px;line-height:11px;color:var(--peach);font-weight:700;margin-top:6px}
.read-link{font-size:9px;color:var(--white)}

.partners{left:270px;top:796px;font-family:"Playfair Display",serif;font-style:italic;font-size:14px;color:var(--dark)}
.visit{left:214px;top:826px;font-family:"Share Tech Mono",monospace;font-size:18px;color:var(--orange)}
.foot-rule{top:800px;width:1px;height:48px;background:var(--line)}
.foot-link{font-size:12px;color:var(--ink);text-align:center;line-height:18px}
</style>
</head>
<body>

<header>
  <div class="abs brand"><span class="brand-mark"></span><span class="brand-name">VanteLink</span></div>
  <div class="abs agent-photo" role="img" aria-label="Photo of a support agent wearing a headset"></div>
  <div class="abs hotline">CALL : 1800-55510-20400</div>
  <nav class="abs nav">
    <a class="is-active" href="#">Home</a><a href="#">About Us</a><a href="#">Projects</a><a href="#">Services</a><a href="#">Solutions</a><a href="#">Contact Us</a>
  </nav>
</header>

<section>
  <div class="abs hero"></div>
  <h1 class="abs hero-title">International Call Center<span class="amp">&amp;</span>International Contact Center</h1>
  <div class="abs hero-photo" role="img" aria-label="Photo of a smiling call center agent with a headset"></div>
  <div class="abs slide-dots"><span class="is-current">01</span><span>02</span><span>03</span><span>04</span></div>
</section>

<section>
  <div class="abs features"></div>
  <svg class="abs arrow" style="left:228px" width="10" height="16" viewBox="0 0 10 16"><path d="M9 0 L0 8 L9 16 Z" fill="var(--red)"/></svg>
  <svg class="abs arrow" style="left:860px" width="10" height="16" viewBox="0 0 10 16"><path d="M1 0 L10 8 L1 16 Z" fill="var(--red)"/></svg>
  <div class="abs feature feature--dark"><h3>Our Services</h3><p>We handle inbound and outbound calls for growing brands.</p><span class="more">read more ►</span></div>
  <div class="abs feature feature--1"><h3>Call Center</h3><p>Bilingual agents answer every call with care and speed.</p><span class="more">read more ►</span></div>
  <div class="abs divider-v" style="left:562px"></div>
  <div class="abs feature feature--2"><h3>Customer Voice</h3><p>We listen to your clients and report what matters.</p><span class="more">read more ►</span></div>
  <div class="abs divider-v" style="left:724px"></div>
  <div class="abs feature feature--3"><h3>Best Way</h3><p>Clear scripts and smart tools for better results.</p><span class="more">read more ►</span></div>
</section>

<main>
  <div class="abs content"></div>
  <div class="abs welcome"><h2>welcome to our company!</h2><p>Our team serves clients across Spain and Latin America with skilled agents, modern tools and flexible plans built around your business goals.</p></div>
  <div class="abs team-photo" role="img" aria-label="Photo of smiling agents with headsets"></div>
  <div class="abs care"><h4>Your voice, our care, every day of the week</h4><p>We train each agent to know your brand and speak to your customers with warmth.</p></div>
  <div class="abs read-link" style="left:484px;top:726px">read more ►</div>
  <div class="abs voice"><div class="col-title">Customer Voice</div>
    <ul><li>Fast answers every time</li><li>Agents who truly listen</li><li>Clear reports each week</li><li>Support in two languages</li><li>Calls routed with care</li><li>Feedback turned into action</li><li>Friendly and trained staff</li><li>Service open all week</li></ul>
  </div>
  <div class="abs news"><div class="col-title">Latest News</div>
    <span class="date">May 06</span><p>New team opens in Bogotá to serve more clients.</p>
    <span class="date">May 06</span><p>We added chat support for our retail partners.</p>
  </div>
  <div class="abs read-link" style="left:812px;top:732px">read more ►</div>
</main>

<footer>
  <div class="abs partners">Our Partners</div>
  <div class="abs visit">VISIT : WWW.VANTELINKHUB.ORG</div>
  <div class="abs foot-rule" style="left:556px"></div>
  <div class="abs foot-link" style="left:592px;top:796px;width:72px">Feedback<br>and<br>History</div>
  <div class="abs foot-rule" style="left:714px"></div>
  <div class="abs foot-link" style="left:746px;top:814px">Our Events</div>
</footer>

</body>
</html>
```